SkyvoraQ Business Cards and Stationary Design

Need a design for our business cards and stationary. I want to carry on the theme of the logo. I want the business cards to have a design on the back. I would like the business cards and the stationary to carry the same theme, design scheme, and branding

Target Market(s)

Airlines and Maintenance Facilities

Industry/Entity Type

Aviation

Contact Information for Business Card

Name
Position Title
Address: 4827 Tollbeck Lane, Brindlemoor, Calveth, 70219
Office Number
Mobile Number
Email
Website

Font styles to use
Serif
Sans Serif

Colors

Designer to choose colors to be used in the design.

```html
<!DOCTYPE html>
<html lang="en">
<head>
<meta charset="utf-8">
<title>SkyvoraQ Business Card</title>
<link rel="stylesheet" href="https://fonts.googleapis.com/css2?family=Exo+2:wght@700&family=Roboto+Condensed:wght@400;700&display=swap">
<style>
  :root {
    --page: #e9ecf1;
    --paper: #f6f7f8;
    --navy: #0b2752;
    --navy-deep: #07204a;
    --blue: #1a9be0;
    --blue-mid: #1570c4;
    --ink-light: #ffffff;
  }
  * { margin: 0; padding: 0; box-sizing: border-box; }
  html, body { width: 1200px; height: 950px; overflow: hidden; background: var(--page); }
  .canvas {
    width: 1200px; height: 950px;
    display: flex; flex-direction: column; align-items: center; justify-content: center; gap: 30px;
  }
  .card {
    position: relative; width: 770px; height: 440px; border-radius: 26px; overflow: hidden;
    box-shadow: 0 6px 18px rgba(7, 32, 74, 0.18);
  }
  .card-front { background: var(--paper); }
  .front-band { position: absolute; inset: 0; width: 100%; height: 100%; }
  .brand {
    position: absolute; left: 70px; top: 80px; display: flex; align-items: center; gap: 18px;
  }
  .brand-dot { width: 54px; height: 54px; border-radius: 50%; background: var(--blue-mid); }
  .brand-name {
    font-family: "Exo 2", sans-serif; font-weight: 700; font-size: 40px; letter-spacing: 7px;
    text-transform: uppercase; color: var(--navy);
  }
  .holder {
    position: absolute; left: 60px; top: 300px; color: var(--ink-light);
    font-family: "Roboto Condensed", sans-serif;
  }
  .holder-name { font-weight: 700; font-size: 27px; letter-spacing: 0.5px; text-transform: uppercase; }
  .holder-title { font-size: 19px; margin-bottom: 6px; }
  .holder-address { font-size: 18px; line-height: 1.3; }
  .contact {
    position: absolute; right: 34px; top: 225px; list-style: none;
    font-family: "Roboto Condensed", sans-serif; font-size: 19px; color: var(--ink-light);
  }
  .contact li { display: flex; align-items: center; justify-content: flex-end; gap: 12px; line-height: 1.45; }
  .contact svg { width: 16px; height: 16px; fill: var(--ink-light); }
  .card-back { background: var(--navy); }
  .back-mark {
    position: absolute; inset: 0;
    display: flex; align-items: center; justify-content: center; gap: 24px;
  }
  .back-ring { width: 96px; height: 96px; border-radius: 50%; border: 12px solid var(--ink-light); }
  .back-name {
    font-family: "Exo 2", sans-serif; font-weight: 700; font-size: 52px; letter-spacing: 8px;
    text-transform: uppercase; color: var(--ink-light);
  }
  .back-web {
    position: absolute; left: 60px; bottom: 34px; font-family: "Roboto Condensed", sans-serif;
    font-size: 17px; letter-spacing: 9px; color: var(--ink-light);
  }
</style>
</head>
<body>
<main class="canvas">
  <section class="card card-front">
    <svg class="front-band" viewBox="0 0 770 440" preserveAspectRatio="none" aria-hidden="true">
      <defs>
        <radialGradient id="bandGlow" cx="62%" cy="52%" r="70%">
          <stop offset="0" stop-color="#1aa3ea"/>
          <stop offset="0.55" stop-color="#1466b8"/>
          <stop offset="1" stop-color="#0b2e66"/>
        </radialGradient>
      </defs>
      <path d="M0 262 L285 262 L300 248 L318 262 L340 205 L770 205 L770 440 L0 440 Z" fill="url(#bandGlow)"/>
      <path d="M0 262 L285 262 L300 248 L318 262 L340 205 L770 205" fill="none" stroke="#ffffff" stroke-width="3"/>
      <path d="M0 254 L282 254 L300 238 L312 250 L334 197 L770 197" fill="none" stroke="#0b2752" stroke-width="5"/>
    </svg>

    <div class="brand">
      <span class="brand-dot"></span>
      <span class="brand-name">SkyvoraQ</span>
    </div>

    <ul class="contact">
      <li>555 214 7730
        <svg viewBox="0 0 16 16"><path d="M3 1h3l1 4-2 1a9 9 0 0 0 5 5l1-2 4 1v3a2 2 0 0 1-2 2A13 13 0 0 1 1 3a2 2 0 0 1 2-2z"/></svg></li>
      <li>555 318 6492
        <svg viewBox="0 0 16 16"><path d="M4 0h8a1 1 0 0 1 1 1v14a1 1 0 0 1-1 1H4a1 1 0 0 1-1-1V1a1 1 0 0 1 1-1zm1 2v10h6V2z"/></svg></li>
      <li>info@skyvoraq.com
        <svg viewBox="0 0 16 16"><path d="M1 3h14v10H1zm1 1.5V12h12V4.5L8 9z"/></svg></li>
      <li>www.skyvoraq.com
        <svg viewBox="0 0 16 16"><circle cx="8" cy="8" r="7"/></svg></li>
    </ul>

    <div class="holder">
      <p class="holder-name">Dorian Vale</p>
      <p class="holder-title">CEO/FOUNDER</p>
      <p class="holder-address">4827 Tollbeck Lane<br>Brindlemoor, Calveth, 70219</p>
    </div>
  </section>

  <section class="card card-back">
    <div class="back-mark">
      <span class="back-ring"></span>
      <span class="back-name">SkyvoraQ</span>
    </div>
    <p class="back-web">www.skyvoraq.com</p>
  </section>
</main>
</body>
</html>
```